Business Card Design for Technology Company

New business card design needed for technology company director.
Ideally, the design will fit the style and nature of the industry. We are a supplier of quality products and services, and we hope the design will give customers and suppliers this impression.

Target Market(s)

3D Printing Industry

Industry/Entity Type

Technology Equipment

Contact Information for Business Card

Name: Marcus Lyle
Title: Director
Company address: Factory K4, 7B Morland Road, Springvale Victoria Australia 3150
Telephone: +61-3-8555 6413
Email: marcus.lyle@veranox.com.au
Website: www.veranox.com.au

Requirements
Must have
• All information in business card details
• Company logo
• '3D Printers and 3D Print Filaments' at proper place
Nice to have
• Style to fit the industry
• Colour to fit logo

```html
<!DOCTYPE html>
<html lang="en">
<head>
<meta charset="utf-8">
<title>Veranox Business Card</title>
<link href="https://fonts.googleapis.com/css2?family=Montserrat:wght@500;700&family=Roboto+Condensed:wght@400;700&display=swap" rel="stylesheet">
<style>
  :root {
    --page: #eceae6;
    --card: #ffffff;
    --ink: #161616;
    --muted: #555555;
    --blue: #1b86c8;
    --orange: #f5820f;
    --grey: #c9cbcc;
    --black: #111111;
  }
  * { box-sizing: border-box; margin: 0; padding: 0; }
  html, body { width: 1200px; height: 1200px; overflow: hidden; background: var(--page); }
  .canvas {
    width: 1200px; height: 1200px;
    display: flex; flex-direction: column; align-items: center; justify-content: center;
    gap: 50px;
  }
  .card {
    position: relative;
    width: 880px; height: 538px;
    background: var(--card);
    box-shadow: 0 6px 20px rgba(0,0,0,0.12);
    overflow: hidden;
  }
  .brand {
    display: flex; align-items: center; gap: 18px;
    font-family: "Montserrat", sans-serif;
    font-weight: 700;
    color: var(--ink);
    letter-spacing: 0.08em;
    text-transform: uppercase;
    white-space: nowrap;
  }
  .brand-mark { background: var(--orange); flex: none; }

  /* back side */
  .card-back .site {
    position: absolute; top: 70px; right: 0;
    display: flex; align-items: center; gap: 14px;
    font-family: "Roboto Condensed", sans-serif;
    font-size: 22px; color: var(--muted);
  }
  .card-back .site::after {
    content: ""; display: block; width: 110px; height: 5px; background: var(--orange);
  }
  .card-back .identity {
    position: absolute; left: 50%; top: 50%;
    transform: translate(-50%, -50%);
    display: flex; flex-direction: column; align-items: center; gap: 22px;
  }
  .card-back .brand { font-size: 78px; }
  .card-back .brand-mark { width: 88px; height: 88px; }
  .tagline {
    font-family: "Montserrat", sans-serif; font-weight: 500;
    font-size: 22px; letter-spacing: 0.04em; color: var(--muted);
    white-space: nowrap;
  }

  /* front side */
  .card-front .name-block {
    position: absolute; top: 70px; left: 0;
    display: flex; align-items: flex-start; gap: 16px;
  }
  .card-front .name-block::before {
    content: ""; display: block; width: 110px; height: 5px; background: var(--blue); margin-top: 12px;
  }
  .name {
    font-family: "Montserrat", sans-serif; font-weight: 700;
    font-size: 46px; color: var(--ink); line-height: 1;
  }
  .role {
    font-family: "Montserrat", sans-serif; font-weight: 500;
    font-size: 22px; color: var(--blue); margin-top: 4px;
  }
  .card-front .brand {
    position: absolute; top: 160px; right: 60px;
    font-size: 46px;
  }
  .card-front .brand-mark { width: 56px; height: 56px; }
  .contacts {
    position: absolute; left: 90px; top: 262px;
    font-family: "Roboto Condensed", sans-serif; font-weight: 700;
    font-size: 25px; color: var(--ink);
    list-style: none;
  }
  .contacts li { display: flex; align-items: center; gap: 14px; height: 34px; }
  .contacts .indent { padding-left: 44px; }
  .icon { width: 28px; height: 28px; flex: none; }
  .band {
    position: absolute; left: 0; right: 0; top: 368px; height: 90px;
    display: flex;
  }
  .band-address {
    flex: 0 0 76%;
    background: var(--blue);
    display: flex; align-items: center; gap: 12px; padding-left: 36px;
    font-family: "Roboto Condensed", sans-serif; font-weight: 700;
    font-size: 20px; color: #fff;
    white-space: nowrap;
  }
  .band-orange { flex: 0 0 9%; background: var(--orange); }
  .band-grey { flex: 0 0 8%; background: var(--grey); }
  .band-black { flex: 1; background: var(--black); }
</style>
</head>
<body>
<main class="canvas">
  <section class="card card-back">
    <p class="site">www.veranox.com.au</p>
    <div class="identity">
      <div class="brand"><span class="brand-mark"></span>Veranox</div>
      <p class="tagline">3D Printers and 3D Print Filaments</p>
    </div>
  </section>

  <section class="card card-front">
    <div class="name-block">
      <div>
        <h1 class="name">Marcus Lyle</h1>
        <p class="role">Director</p>
      </div>
    </div>
    <div class="brand"><span class="brand-mark"></span>Veranox</div>
    <ul class="contacts">
      <li>
        <svg class="icon" viewBox="0 0 28 28" aria-hidden="true">
          <circle cx="14" cy="14" r="12" fill="none" stroke="var(--blue)" stroke-width="1.6"/>
          <path d="M10 8.5c.8-.6 1.6-.4 2 .4l1 2c.3.7 0 1.2-.5 1.6l-.7.5c.6 1.5 1.7 2.6 3.2 3.2l.5-.7c.4-.5.9-.8 1.6-.5l2 1c.8.4 1 1.2.4 2-1.2 1.5-3 1.6-5 .4-2.5-1.5-4.3-3.3-5.3-5.8-.8-2-.5-3.4.8-4.1z" fill="var(--blue)"/>
        </svg>
        +61-3-8555 6413
      </li>
      <li>
        <svg class="icon" viewBox="0 0 28 28" aria-hidden="true">
          <circle cx="14" cy="14" r="12" fill="var(--blue)"/>
          <g fill="none" stroke="#fff" stroke-width="1.3">
            <circle cx="14" cy="14" r="7"/>
            <ellipse cx="14" cy="14" rx="3" ry="7"/>
            <line x1="7" y1="14" x2="21" y2="14"/>
          </g>
        </svg>
        marcus.lyle@veranox.com.au
      </li>
      <li class="indent">www.veranox.com.au</li>
    </ul>
    <div class="band">
      <div class="band-address">
        <svg class="icon" viewBox="0 0 28 28" aria-hidden="true">
          <circle cx="14" cy="14" r="12" fill="#fff"/>
          <path d="M14 6.5a5 5 0 0 0-5 5c0 3.8 5 9.5 5 9.5s5-5.7 5-9.5a5 5 0 0 0-5-5z" fill="var(--blue)"/>
          <circle cx="14" cy="11.5" r="1.8" fill="#fff"/>
        </svg>
        Factory K4, 7B Morland Road, Springvale Victoria Australia 3150
      </div>
      <div class="band-orange"></div>
      <div class="band-grey"></div>
      <div class="band-black"></div>
    </div>
  </section>
</main>
</body>
</html>
```